Larkwell Moments Studio Website
looking for wow/drama
Larkwell Moments Studio Website - Events
Creative Brief
Events
www.larkwellmoments.example
Based in Greater Boston, Larkwell Moments Studio is a boutique custom events and marketing firm.
Looking for dramatic layout/bold. Clean and simple...DRAMA/showstopper! I like texture would prefer navigation to be unique - located in a new place/different layout -- unexpected I WANT A VERY UNIQUE LAYOUT Don't like: anything ordinary/hate wehn things feel "flat"
Black
Teal (the exact teal of my logo)
White and dark Grey accents (from my logo)
right side
http://www.doranpeswick.example/
http://www.thebrightorchard.example/
http://www.velvetaffairs.example.uk/
drama wins. I will not have much "copy" cluttering up my website, The look of the website needs to be a showstopper. other websites: http://www.zintrova.example.uk/ (unique layout) http://www.quillmarshband.example.uk/index4.php http://www.brantoloft.example/

```html
<!DOCTYPE html>
<html lang="en">
<head>
<meta charset="utf-8">
<title>Larkwell Moments Studio</title>
<link rel="stylesheet" href="https://fonts.googleapis.com/css2?family=Italianno&family=Poiret+One&family=Open+Sans:wght@400;600&display=swap">
<style>
  :root {
    --teal: #1fa7b4;
    --ink: #222222;
    --grey: #5c5c5c;
    --text-grey: #8a8a8a;
    --panel: #ffffff;
    --panel-shade: #ececec;
    --frame: #bdbdbd;
  }
  * { box-sizing: border-box; margin: 0; padding: 0; }
  html, body { width: 1200px; height: 804px; overflow: hidden; }
  body {
    position: relative;
    font-family: "Open Sans", Arial, sans-serif;
    color: var(--ink);
    background: #eef3f6;
  }
  .backdrop {
    position: absolute; inset: 0;
    background:
      radial-gradient(ellipse 420px 300px at 80px 120px, rgba(170,200,235,.55), transparent 70%),
      radial-gradient(ellipse 420px 360px at 1120px 120px, rgba(235,200,215,.55), transparent 70%),
      radial-gradient(ellipse 500px 300px at 1050px 760px, rgba(240,215,185,.5), transparent 70%),
      radial-gradient(ellipse 500px 320px at 160px 780px, rgba(190,225,210,.5), transparent 70%),
      radial-gradient(ellipse 600px 360px at 600px 60px, rgba(215,230,200,.45), transparent 70%),
      linear-gradient(135deg, #e9f0f7, #f4eef1 50%, #f2efe6);
  }

  /* brand */
  .brand-mark {
    position: absolute; left: 234px; top: 72px; z-index: 3;
    width: 124px; height: 78px; border-radius: 50% 50% 0 0 / 100% 100% 0 0;
    background: linear-gradient(180deg, #f4f4f4, #dcdcdc);
    border: 2px solid #cfcfcf; border-bottom: none;
  }
  .brand {
    position: absolute; left: 163px; top: 156px; z-index: 3;
    font-family: "Poiret One", "Century Gothic", sans-serif;
    color: var(--ink);
  }
  .brand-name { font-size: 48px; line-height: 1; letter-spacing: 1px; }
  .brand-tag { font-size: 15px; line-height: 22px; margin-top: 6px; letter-spacing: .5px; }

  /* navigation */
  .main-nav {
    position: absolute; left: 552px; top: 84px;
    display: flex; gap: 42px;
    font-family: "Italianno", "Monotype Corsiva", cursive;
    font-size: 44px; line-height: 1;
  }
  .main-nav a { color: var(--ink); text-decoration: none; }
  .main-nav a.is-active { color: var(--teal); }
  .submenu {
    position: absolute; left: 782px; top: 134px; z-index: 4;
    width: 120px; height: 124px;
    background: var(--panel);
    box-shadow: 0 2px 6px rgba(0,0,0,.15);
    padding: 16px 0 0 20px;
    list-style: none;
    font-size: 14px; line-height: 34px;
  }
  .submenu::before {
    content: ""; position: absolute; left: 76px; top: 2px;
    border: 9px solid transparent; border-top-color: var(--teal);
  }
  .contact-tab {
    position: absolute; left: 1050px; top: 184px; z-index: 4;
    width: 104px; height: 38px;
    background: var(--teal);
    clip-path: polygon(8% 0, 100% 0, 100% 100%, 0 100%);
    color: #fff; font-family: "Italianno", cursive; font-size: 36px;
    line-height: 40px; padding-left: 20px; text-decoration: none;
  }

  /* panel */
  .panel-band {
    position: absolute; left: 126px; top: 140px;
    width: 994px; height: 560px; border-radius: 32px;
    background: var(--teal);
  }
  .panel {
    position: absolute; left: 138px; top: 138px; z-index: 2;
    width: 980px; height: 552px; border-radius: 30px;
    background: linear-gradient(180deg, var(--panel) 0%, #f7f7f7 60%, var(--panel-shade) 100%);
    overflow: hidden;
  }
  .ornament {
    position: absolute; right: 0; bottom: 0;
    width: 350px; height: 225px;
    background: radial-gradient(ellipse at 70% 70%, rgba(31,167,180,.55), rgba(31,167,180,.15) 60%, transparent 80%);
  }

  .welcome {
    position: absolute; left: 163px; top: 305px; z-index: 3;
    font-family: "Poiret One", "Century Gothic", sans-serif;
    font-weight: 400; font-size: 46px; letter-spacing: 1px; line-height: 1;
    white-space: nowrap;
  }
  .intro {
    position: absolute; left: 197px; top: 374px; z-index: 3;
    width: 500px;
    font-size: 13.5px; line-height: 24.5px; color: var(--text-grey);
  }
  .quote-mark {
    position: absolute; z-index: 3; color: var(--teal);
    font-family: Georgia, serif; font-size: 48px; line-height: 1;
  }
  .quote-open { left: 163px; top: 366px; }
  .quote-close { left: 612px; top: 626px; }

  .photo-slot {
    position: absolute; z-index: 3;
    width: 196px; height: 148px;
    background: #fafafa; border: 6px solid var(--frame);
    box-shadow: 2px 3px 8px rgba(0,0,0,.3);
  }
  .photo-back { left: 726px; top: 282px; transform: rotate(12deg); }
  .photo-front {
    left: 716px; top: 308px; background: var(--panel-shade);
    display: flex; align-items: center; justify-content: center;
    font-size: 15px; color: var(--ink); font-weight: 600;
  }

  /* footer */
  .site-footer { position: absolute; top: 712px; font-size: 14px; color: var(--grey); }
  .copyright { left: 163px; }
  .copyright span { color: var(--teal); }
  .contact-line { left: 768px; display: flex; gap: 44px; }
</style>
</head>
<body>
  <div class="backdrop" role="img" aria-label="Soft pastel watercolour wash background"></div>

  <nav class="main-nav">
    <a href="#">Home</a>
    <a href="#">About</a>
    <a href="#" class="is-active">Services</a>
    <a href="#">Gallery</a>
  </nav>
  <ul class="submenu">
    <li>Services</li>
    <li>Philosophy</li>
    <li>Owner</li>
  </ul>
  <a class="contact-tab" href="#">Contact</a>

  <div class="panel-band" aria-hidden="true"></div>
  <main class="panel">
    <div class="ornament" role="img" aria-label="Teal flourish swirl ornament"></div>
  </main>

  <div class="brand-mark" aria-hidden="true"></div>
  <div class="brand">
    <div class="brand-name">LARKWELL</div>
    <div class="brand-tag">Moments Studio<br>Custom Events &amp; Marketing</div>
  </div>

  <h1 class="welcome">WELCOME TO LARKWELL</h1>
  <span class="quote-mark quote-open">&ldquo;</span>
  <p class="intro">Lorem ipsum dolor sit amet, consectetuer adipiscing elit, sed diam nonummy nibh euismod tincidunt ut laoreet dolore magna aliquam erat volutpat. Ut wisi enim ad lorem ipsum dolor sit amet, consectetuer adipiscing elit, sed diam nonummy nibh euismod tincidunt ut laoreet dolore magna aliquam erat volutpat. Ut wisi enim nonummy nibh euismod tincidunt ut laoreet dolore magna aliquam erat volutpat. Ut wisi enim ad lorem ipsum dolor sit amet, consectetuer adipiscing elit, sed diam nonummy nibh euismod tincidunt ut laoreet dolore magna aliquam erat volutpat. Ut wisi enim ad nonummy nibh euismod tincidunt ut laoreet dolore magna aliquam erat volutpat. Ut wisi enim ad</p>
  <span class="quote-mark quote-close">&rdquo;</span>

  <div class="photo-slot photo-back" aria-hidden="true"></div>
  <div class="photo-slot photo-front">image here</div>

  <footer>
    <p class="site-footer copyright"><span>&copy;2011:</span> Larkwell</p>
    <p class="site-footer contact-line"><span>ask@larkwellmoments.example</span><span>555-204-7716</span></p>
  </footer>
</body>
</html>
```